Business Card - connecting 2 souls and beggining the journey of self discovery

Logo on the front
with tag line

On the back list of services and contact details

Seminars
workshops
Coaching
podcasts

Daniel Porthwick
Health & Wellbeing Life Coach
0491 372 815
daniel@wovenpathwellness.example
wovenpathwellness.example

Industry/Entity Type

Life Coaching

Contact Information for Business Card

I like the use of colour from the logo to be used. I'm not a fan of white.

Requirements
Must have
• My tagline: The journey home starts with you
Nice to have
• Use of colour that is in the mind body soul logo

```html
<!DOCTYPE html>
<html lang="en">
<head>
<meta charset="utf-8">
<title>Woven Path Wellness – Business Card</title>
<link rel="stylesheet" href="https://fonts.googleapis.com/css2?family=Source+Sans+3:wght@400;600&display=swap">
<style>
  :root {
    --backdrop: #c4c4c4;
    --card-grey: #838688;
    --card-white: #ffffff;
    --text-grey: #7d8083;
    --name-purple: #7b4f9e;
    --icon-orange: #f5a21b;
    --divider: #c9d977;
    --mark-coral: #f2766a;
    --accent-curve: #8a6aa8;
    --white: #ffffff;
  }
  * { margin: 0; padding: 0; box-sizing: border-box; }
  html, body {
    width: 1200px; height: 947px; overflow: hidden;
    background: var(--backdrop);
    font-family: "Source Sans 3", Arial, sans-serif;
  }
  .card {
    position: absolute; left: 263px; width: 674px; height: 385px;
    box-shadow: -3px 3px 6px rgba(0,0,0,.3);
  }
  /* Front */
  .card--front { top: 82px; background: var(--card-grey); color: var(--white); text-align: center; }
  .brand-dot {
    position: absolute; left: 273px; top: 98px; width: 128px; height: 128px;
    border-radius: 50%; background: var(--mark-coral);
  }
  .card--front .brand-name {
    position: absolute; left: 0; right: 0; top: 250px;
    font-size: 36px; font-weight: 400; letter-spacing: -0.5px; line-height: 44px;
  }
  .tagline {
    position: absolute; left: 0; right: 0; top: 333px;
    font-size: 18px; font-weight: 400; line-height: 24px;
  }
  /* Back */
  .card--back { top: 482px; background: var(--card-white); overflow: hidden; }
  .brand-block { position: absolute; left: 24px; top: 130px; width: 300px; text-align: center; }
  .brand-block .brand-dot { position: static; display: block; margin: 0 auto; width: 86px; height: 86px; }
  .brand-block .brand-name {
    margin-top: 10px; font-size: 25px; font-weight: 400; color: var(--text-grey);
    letter-spacing: -0.3px; line-height: 30px;
  }
  .divider { position: absolute; left: 324px; top: 128px; width: 2px; height: 133px; background: var(--divider); }
  .contact { position: absolute; left: 344px; top: 120px; color: var(--text-grey); }
  .person-name { font-size: 26px; font-weight: 600; color: var(--name-purple); line-height: 32px; }
  .person-role { font-size: 17px; font-weight: 600; line-height: 22px; }
  .contact-list { list-style: none; margin-top: 20px; }
  .contact-list li { display: flex; align-items: center; gap: 7px; font-size: 17px; font-weight: 600; line-height: 22px; }
  .contact-list svg { width: 14px; height: 14px; flex: none; }
  .footer-band { position: absolute; left: 0; top: 0; width: 674px; height: 385px; }
  .services {
    position: absolute; left: 0; right: 0; top: 345px; text-align: center;
    color: var(--white); font-size: 18px; line-height: 24px;
  }
  .services span { margin: 0 8px; font-size: 14px; }
</style>
</head>
<body>
  <section class="card card--front">
    <span class="brand-dot"></span>
    <h1 class="brand-name">Woven Path Wellness</h1>
    <p class="tagline">The journey home starts with you</p>
  </section>

  <section class="card card--back">
    <svg class="footer-band" viewBox="0 0 674 385" aria-hidden="true">
      <path d="M0,359 Q337,298 674,359 Q337,322 0,359 Z" fill="var(--accent-curve)"/>
      <path d="M0,385 L0,365 Q337,322 674,365 L674,385 Z" fill="var(--card-grey)"/>
    </svg>

    <div class="brand-block">
      <span class="brand-dot"></span>
      <p class="brand-name">Woven Path Wellness</p>
    </div>

    <span class="divider"></span>

    <div class="contact">
      <h2 class="person-name">Daniel Porthwick</h2>
      <p class="person-role">Life Coach</p>
      <ul class="contact-list">
        <li>
          <svg viewBox="0 0 16 16"><path d="M3 1h3l1.5 4-2 1.3a8 8 0 0 0 4.2 4.2L11 8.5 15 10v3a2 2 0 0 1-2 2A12 12 0 0 1 1 3a2 2 0 0 1 2-2z" fill="var(--icon-orange)"/></svg>
          0491 372 815
        </li>
        <li>
          <svg viewBox="0 0 16 16"><rect x="1" y="3" width="14" height="10" fill="none" stroke="var(--icon-orange)" stroke-width="1.6"/><path d="M1 3l7 6 7-6" fill="none" stroke="var(--icon-orange)" stroke-width="1.6"/></svg>
          daniel@wovenpathwellness.example
        </li>
        <li>
          <svg viewBox="0 0 16 16" fill="none" stroke="var(--icon-orange)" stroke-width="1.4"><circle cx="8" cy="8" r="6.5"/><ellipse cx="8" cy="8" rx="3" ry="6.5"/><path d="M1.5 8h13M2.5 4.8h11M2.5 11.2h11"/></svg>
          wovenpathwellness.example
        </li>
      </ul>
    </div>

    <p class="services">Seminars<span>•</span>Workshops<span>•</span>Coaching<span>•</span>Podcasts</p>
  </section>
</body>
</html>
```